Rack Card Design Project

Brevik Yachts is a yacht charter company. We have a new 49 passenger, very modern interior, luxury yacht that we want to feature in this card.

```html
<!DOCTYPE html>
<html lang="en">
<head>
<meta charset="utf-8">
<title>Brevik Yachts Rack Card</title>
<link rel="stylesheet" href="https://fonts.googleapis.com/css2?family=Arvo&family=Open+Sans:wght@400;600&display=swap">
<style>
  :root {
    --stage: #5a5a5a;
    --blue-light: #3559c8;
    --blue-deep: #1a2d8c;
    --red: #a01515;
    --white: #ffffff;
    --sunset: #c8a9b6;
    --sea: #4a5d86;
    --party: #8a8f98;
    --bar: #6b5a4c;
  }
  * { margin: 0; padding: 0; box-sizing: border-box; }
  html, body { width: 826px; height: 1200px; overflow: hidden; }
  body { background: var(--stage); position: relative; font-family: "Open Sans", sans-serif; }

  .rack-card {
    position: absolute; left: 169px; top: 50px;
    width: 489px; height: 1101px;
    background: radial-gradient(ellipse at 50% 55%, var(--blue-light) 0%, var(--blue-deep) 85%);
    overflow: hidden;
  }
  .photo { position: absolute; }
  .photo-yacht {
    left: 0; top: 0; width: 489px; height: 307px;
    background: linear-gradient(180deg, var(--sunset) 0%, #b89aa6 30%, var(--sea) 100%);
  }
  .photo-guests {
    left: 0; top: 317px; width: 239px; height: 280px;
    background: linear-gradient(160deg, #aab6c4 0%, var(--party) 60%, #6d6a70 100%);
  }
  .photo-bartender {
    left: 250px; top: 317px; width: 239px; height: 280px;
    background: linear-gradient(200deg, #8c7a68 0%, var(--bar) 55%, #4f4a4c 100%);
  }
  .wave { position: absolute; left: 0; top: 500px; width: 489px; height: 140px; }

  .brand-name {
    position: absolute; left: 28px; top: 540px;
    font-family: "Arvo", serif; font-size: 30px; color: var(--white);
  }

  .headline {
    position: absolute; left: 0; top: 630px; width: 489px;
    text-align: center; font-family: "Arvo", serif; font-size: 33px;
    line-height: 37px; color: var(--white); letter-spacing: 0.3px;
  }
  .intro {
    position: absolute; left: 0; top: 709px; width: 489px;
    text-align: center; font-size: 17px; line-height: 23px; color: var(--white);
  }
  .features { position: absolute; left: 0; top: 0; width: 489px; list-style: none; color: var(--white); font-size: 16px; line-height: 22px; }
  .features li { position: absolute; white-space: nowrap; padding-left: 18px; }
  .features li svg { position: absolute; left: 0; top: 7px; width: 11px; height: 10px; }
  .features .cont { padding-left: 0; }

  .cta {
    position: absolute; left: 0; top: 948px; width: 489px;
    text-align: center; font-size: 31px; font-weight: 600; color: var(--white); line-height: 40px;
  }
  .phone {
    position: absolute; left: 48px; top: 989px; width: 393px; height: 50px;
    background: var(--red); border-radius: 12px;
    text-align: center; font-size: 43px; line-height: 50px; color: var(--white);
  }
  .website {
    position: absolute; left: 0; top: 1044px; width: 489px;
    text-align: center; font-size: 31px; color: var(--white); line-height: 40px;
  }
</style>
</head>
<body>
  <main class="rack-card">
    <div class="photo photo-yacht" role="img" aria-label="Guests on the deck of a white motor yacht cruising San Diego Bay at sunset"></div>
    <div class="photo photo-guests" role="img" aria-label="Young guests smiling with drinks aboard a yacht at the marina"></div>
    <div class="photo photo-bartender" role="img" aria-label="Bartender pouring a drink at the yacht's bar"></div>

    <svg class="wave" viewBox="0 0 489 140" preserveAspectRatio="none" aria-hidden="true">
      <path d="M0 80 C 150 95, 330 80, 489 22 L489 140 L0 140 Z" fill="var(--white)"/>
      <path d="M0 82 C 150 96, 330 82, 489 26 L489 44 C 380 90, 220 110, 0 104 Z" fill="var(--red)"/>
      <path d="M0 104 C 220 110, 380 90, 489 44 L489 48 C 380 96, 220 116, 0 110 Z" fill="var(--white)"/>
      <path d="M0 110 C 220 116, 380 96, 489 48 L489 140 L0 140 Z" fill="#2343b0"/>
    </svg>

    <div class="brand-name">Brevik Yachts</div>

    <h1 class="headline">A UNIQUE WAY TO<br>EXPERIENCE SAN DIEGO</h1>
    <p class="intro">Brevik Yachts offers lodging aboard our pristine yachts<br>on San Diego Bay</p>

    <ul class="features">
      <li style="left:35px; top:776px;"><svg viewBox="0 0 11 10"><path d="M1 5 L4 8.5 L10 1" fill="none" stroke="#fff" stroke-width="1.4"/></svg>Multiple Yachts &amp; Houseboat on Harbor Island</li>
      <li style="left:35px; top:801px;"><svg viewBox="0 0 11 10"><path d="M1 5 L4 8.5 L10 1" fill="none" stroke="#fff" stroke-width="1.4"/></svg>Just minutes from the airport &amp; downtown San Diego</li>
      <li style="left:35px; top:830px;"><svg viewBox="0 0 11 10"><path d="M1 5 L4 8.5 L10 1" fill="none" stroke="#fff" stroke-width="1.4"/></svg>Access to Marina pool &amp; Harborview Hotel amenities</li>
      <li class="cont" style="left:53px; top:852px;">(Pools, Gym &amp; Spa)</li>
      <li style="left:35px; top:879px;"><svg viewBox="0 0 11 10"><path d="M1 5 L4 8.5 L10 1" fill="none" stroke="#fff" stroke-width="1.4"/></svg>Nearby Restaurants</li>
      <li style="left:214px; top:879px;"><svg viewBox="0 0 11 10"><path d="M1 5 L4 8.5 L10 1" fill="none" stroke="#fff" stroke-width="1.4"/></svg>Affordable Overnight Lodging</li>
      <li style="left:35px; top:907px;"><svg viewBox="0 0 11 10"><path d="M1 5 L4 8.5 L10 1" fill="none" stroke="#fff" stroke-width="1.4"/></svg>Spectacular Views</li>
      <li style="left:214px; top:907px;"><svg viewBox="0 0 11 10"><path d="M1 5 L4 8.5 L10 1" fill="none" stroke="#fff" stroke-width="1.4"/></svg>Optional Harbor Cruises</li>
    </ul>

    <p class="cta">CONTACT US TODAY</p>
    <p class="phone">555-014-2290</p>
    <p class="website">www.brevikyachts.com</p>
  </main>
</body>
</html>
```